New banner design for mortgage broker

Looking for a banner design for mortgage broking company.
- need to use logo
- need to use colours from the logo
- like to use the headshot somehow.
- use slogan ' Helping to navigate your finance journey'
- include listing our services. Home Loans, Investment Loans, First Home Buyers, Self-employed Specialist, Car loans, Past Credit issues.
- call to action to get in contact today on 1300 642 917 or www.harbourfinvo.com.au
- Banner size 2.4m x 0.6m

```html
<!DOCTYPE html>
<html lang="en">
<head>
<meta charset="utf-8">
<title>Harbour Lending Group – Banner</title>
<link rel="stylesheet" href="https://fonts.googleapis.com/css2?family=Nunito+Sans:wght@400;600;700;800;900&display=swap">
<style>
  :root {
    --purple: #552d82;
    --white: #ffffff;
    --paper: #fbfbfd;
    --ink-soft: #4f4f55;
    --backdrop: #e3e3e3;
    --photo-light: #d9d6d2;
    --photo-dark: #8a7a6c;
  }
  * { margin: 0; padding: 0; box-sizing: border-box; }
  html, body { width: 1200px; height: 330px; overflow: hidden; }
  body {
    background: var(--backdrop);
    font-family: "Nunito Sans", Arial, sans-serif;
    position: relative;
  }
  .banner {
    position: absolute; left: 46px; top: 27px;
    width: 1110px; height: 277px;
    background: var(--paper);
    box-shadow: 0 1px 3px rgba(0,0,0,.25);
    overflow: hidden;
  }
  .advisor { position: absolute; left: 0; top: 0; width: 280px; height: 277px; }
  .advisor svg { position: absolute; left: 0; top: 0; }
  .advisor-name {
    position: absolute; left: 34px; top: 242px;
    color: var(--white); font-size: 14px; white-space: nowrap;
  }
  .advisor-name .role { font-size: 10.5px; }

  .message { position: absolute; left: 309px; top: 28px; width: 250px; }
  .slogan {
    color: var(--purple); font-weight: 900;
    font-size: 32px; line-height: 34px; letter-spacing: -0.2px;
  }
  .intro {
    margin-top: 19px; color: var(--ink-soft);
    font-size: 14px; line-height: 17.5px; width: 220px;
  }

  .services {
    position: absolute; left: 566px; top: 0; width: 297px; height: 277px;
    background: var(--purple); color: var(--white);
  }
  .services h2 {
    position: absolute; left: 51px; top: 20px;
    font-size: 23px; font-weight: 800;
  }
  .service-list { position: absolute; left: 51px; top: 64px; width: 187px; list-style: none; }
  .service-list li {
    display: flex; align-items: center;
    border-bottom: 1px solid rgba(255,255,255,.75);
    font-size: 16.5px; line-height: 17px;
    height: 30px;
  }
  .service-list li.tall { height: 46px; }
  .service-list li:last-child { border-bottom: none; }
  .service-list svg { flex: none; margin: 0 12px 0 6px; }

  .contact { position: absolute; left: 863px; top: 0; width: 247px; height: 277px; }
  .brand {
    height: 114px; background: var(--white);
    display: flex; align-items: center; justify-content: center; gap: 8px;
    color: var(--purple);
  }
  .brand-name { font-size: 19px; font-weight: 700; line-height: 21px; letter-spacing: .5px; }
  .cta {
    height: 163px; background: var(--purple); color: var(--white);
    text-align: center; position: relative;
  }
  .cta-label { position: absolute; left: 0; right: 0; top: 34px; font-size: 23px; }
  .cta-phone {
    position: absolute; left: 20px; top: 86px;
    display: flex; align-items: center; gap: 9px;
    font-size: 22.5px; font-weight: 800;
  }
  .cta-web { position: absolute; left: 0; right: 0; top: 128px; font-size: 16px; }
</style>
</head>
<body>
  <main class="banner">
    <section class="advisor">
      <svg width="280" height="277" viewBox="0 0 280 277">
        <defs>
          <radialGradient id="portraitTone" cx="50%" cy="45%" r="60%">
            <stop offset="0" stop-color="var(--photo-light)"/>
            <stop offset="1" stop-color="var(--photo-dark)"/>
          </radialGradient>
        </defs>
        <path d="M0 145 H154 V0 H261 Q280 0 280 19 V277 H0 Z" fill="var(--purple)"/>
        <circle cx="159" cy="120" r="119" fill="var(--white)" stroke="var(--purple)" stroke-width="2"/>
        <circle cx="159" cy="120" r="116" fill="url(#portraitTone)" role="img" aria-label="Headshot of the senior finance advisor"/>
      </svg>
      <p class="advisor-name">Claire Morgan | <span class="role">Senior Finance Advisor</span></p>
    </section>

    <section class="message">
      <h1 class="slogan">“Helping to navigate your finance journey”</h1>
      <p class="intro">We’re here to guide you through every step of your financial journey with expert advice and tailored solutions</p>
    </section>

    <section class="services">
      <h2>Services Offers:</h2>
      <ul class="service-list">
        <li><svg width="18" height="18" viewBox="0 0 18 18"><path d="M14 9v7H2V3h10" fill="none" stroke="#fff" stroke-width="2"/><path d="M5 8l3 3 8-9" fill="none" stroke="#fff" stroke-width="2.2"/></svg>Home Loans</li>
        <li><svg width="18" height="18" viewBox="0 0 18 18"><path d="M14 9v7H2V3h10" fill="none" stroke="#fff" stroke-width="2"/><path d="M5 8l3 3 8-9" fill="none" stroke="#fff" stroke-width="2.2"/></svg>Investment Loans</li>
        <li><svg width="18" height="18" viewBox="0 0 18 18"><path d="M14 9v7H2V3h10" fill="none" stroke="#fff" stroke-width="2"/><path d="M5 8l3 3 8-9" fill="none" stroke="#fff" stroke-width="2.2"/></svg>First Home Buyers</li>
        <li class="tall"><svg width="18" height="18" viewBox="0 0 18 18"><path d="M14 9v7H2V3h10" fill="none" stroke="#fff" stroke-width="2"/><path d="M5 8l3 3 8-9" fill="none" stroke="#fff" stroke-width="2.2"/></svg>Self-employed<br>Specialist</li>
        <li><svg width="18" height="18" viewBox="0 0 18 18"><path d="M14 9v7H2V3h10" fill="none" stroke="#fff" stroke-width="2"/><path d="M5 8l3 3 8-9" fill="none" stroke="#fff" stroke-width="2.2"/></svg>Car loans</li>
        <li><svg width="18" height="18" viewBox="0 0 18 18"><path d="M14 9v7H2V3h10" fill="none" stroke="#fff" stroke-width="2"/><path d="M5 8l3 3 8-9" fill="none" stroke="#fff" stroke-width="2.2"/></svg>Past Credit issues</li>
      </ul>
    </section>

    <section class="contact">
      <div class="brand">
        <svg width="26" height="26" viewBox="0 0 26 26"><circle cx="13" cy="13" r="11" fill="none" stroke="var(--purple)" stroke-width="3"/></svg>
        <p class="brand-name">Harbour<br>Lending Group</p>
      </div>
      <div class="cta">
        <p class="cta-label">Call-to-Action:</p>
        <p class="cta-phone">
          <svg width="34" height="34" viewBox="0 0 34 34"><circle cx="17" cy="17" r="17" fill="#fff"/><path d="M12 9c1-1 2-1 3 0l2 3c.6 1 .3 1.8-.5 2.4l-1 .8c.8 2 2.4 3.6 4.4 4.4l.8-1c.6-.8 1.4-1.1 2.4-.5l3 2c1 1 1 2 0 3l-1.5 1.5C22 26 17 24 13.5 20.5S8 12 9.5 10.5Z" fill="var(--purple)"/></svg>
          1300 642 917
        </p>
        <p class="cta-web">www.harbourfinvo.com.au</p>
      </div>
    </section>
  </main>
</body>
</html>
```